Medicinal Cannabis Patient Monitoring App

We have a BASIC design for our app for monitoring patients who received Medicinal Cannabis.
The patient would rate how they're feeling after each dose.

The general flow once user is logged in and set up in the system is:

- User should be able to enter the dosing information for the current day
* Consumption Details:
> Enter Time
> Enter Dosage Taken (Added during onboarding)
> Method take to consume the drug
* Score Details:
> Pain Score (On the scale of 1-10)
> Nausea Score (On the scale of 1-10)
> Sedation Score (On the scale of 1-10)
> Wellbeing Score (On the scale of 1-10)
* Blood Pressure Details:
> Pulse
> Blood Pressure Readings
- User should be able to view the instructions
- User should be able to submit the entered details in the platform

We're looking for a clean, medical and SIMPLE design.

OUR USERS are often ELDERLY, Children and disabled individuals. You must consider this in the design.
So, for example, when designing sliders you should consider a creative way to explain the meaning of the slider if the person cant read the word description.

Designs look the same

```html
<!DOCTYPE html>
<html lang="en">
<head>
<meta charset="utf-8">
<title>Greenleaf Care Monitor – App Screens</title>
<link rel="stylesheet" href="https://fonts.googleapis.com/css2?family=Open+Sans:wght@400;600;700;800&display=swap">
<style>
  :root {
    --board: #444444;
    --header-green: #64a11a;
    --btn-light: #9fd12e;
    --btn-dark: #6bb31c;
    --white: #ffffff;
    --ink: #1e1e1e;
    --muted: #8a8a8a;
    --field: #f0f0f0;
    --field-line: #cfcfcf;
    --footer: #e4e4e4;
    --panel-grey: #f1f1f1;
    --tick: #9a9a9a;
  }
  * { box-sizing: border-box; margin: 0; padding: 0; }
  html, body { width: 848px; height: 1200px; overflow: hidden; }
  body { background: var(--board); font-family: "Open Sans", Arial, sans-serif; color: var(--ink); position: relative; }

  .screen { position: absolute; width: 352px; height: 527px; background: var(--white); overflow: hidden; }
  .screen--feeling { left: 56px; top: 56px; }
  .screen--start { left: 440px; top: 56px; }
  .screen--dose { left: 56px; top: 617px; }
  .screen--readings { left: 440px; top: 617px; }

  .app-header { height: 70px; background: var(--header-green); color: var(--white); text-align: center;
    font-weight: 700; font-size: 22.5px; line-height: 25px; padding-top: 10px; letter-spacing: .2px; }
  .app-footer { position: absolute; left: 0; bottom: 0; width: 100%; height: 38px; background: var(--footer);
    font-size: 9px; color: var(--ink); text-align: center; padding-top: 13px; }
  .app-footer .code { position: absolute; right: 6px; bottom: 3px; font-size: 8.5px; }

  .abs { position: absolute; }

  /* Feeling screen */
  .feeling-title { left: 0; width: 100%; top: 108px; text-align: center; font-size: 22px; font-weight: 400; }
  .scale { left: 11px; width: 330px; height: 50px; }
  .scale svg { display: block; }
  .scale-label { position: absolute; top: 28px; font-size: 10.5px; font-weight: 600; letter-spacing: .3px; }
  .scale-label.min { left: 6px; }
  .scale-label.max { right: 0; }
  .scale-label.name { left: 0; width: 100%; text-align: center; }

  /* Start screen */
  .hero-photo { left: 0; top: 70px; width: 352px; height: 193px;
    background: linear-gradient(120deg, #5b6a59 0%, #6f7d6a 30%, #7fa3b8 55%, #a9c6d6 100%); }
  .pill-button { display: flex; align-items: center; justify-content: center; color: var(--white);
    font-weight: 700; border-radius: 30px;
    background: linear-gradient(180deg, var(--btn-light) 0%, var(--btn-light) 50%, var(--btn-dark) 50%, var(--btn-dark) 100%); }
  .start-button { left: 12px; top: 355px; width: 329px; height: 45px; font-size: 16px; letter-spacing: .4px; gap: 6px; }

  /* Dose screen */
  .section-title { left: 0; width: 100%; text-align: center; font-weight: 700; font-size: 16px; letter-spacing: .2px; }
  .time-picker { left: 11px; top: 119px; width: 330px; background: var(--panel-grey); }
  .picker-row { position: relative; display: block; border-bottom: 1px solid #d6d6d6; }
  .picker-row span { position: absolute; top: 50%; transform: translate(-50%, -50%); white-space: nowrap; }
  .picker-row.far { height: 29px; font-size: 8.5px; color: var(--muted); }
  .picker-row.near { height: 25px; font-size: 11.5px; color: #333; }
  .picker-row.near .num { font-weight: 700; font-size: 10px; }
  .picker-row.far .num { font-weight: 600; }
  .picker-row.current { height: 37px; background: var(--white); font-size: 17px; border-top: 1px solid #d6d6d6; }
  .picker-row.current .num { font-weight: 700; font-size: 18px; }
  .picker-row.current .divider { position: absolute; top: 0; width: 1px; height: 100%; background: #d6d6d6; transform: none; }
  .picker-row:last-child { border-bottom: 0; }
  .c-day { left: 56px; } .c-hour { left: 134px; } .c-colon { left: 164px; } .c-min { left: 204px; } .c-ampm { left: 287px; }

  .dose-field { left: 86px; top: 319px; width: 180px; height: 32px; background: var(--field); border: 1px solid var(--field-line);
    border-radius: 2px; font-size: 13px; color: var(--muted); text-align: right; padding: 5px 9px 0 0; }
  .method { top: 382px; display: flex; align-items: center; gap: 6px; font-size: 14.5px; }
  .method .box { width: 11px; height: 11px; border: 1px solid #8f8f8f; background: var(--white); border-radius: 2px; position: relative; }
  .method .box.checked::after { content: ""; position: absolute; left: 2px; top: 2px; width: 5px; height: 5px; border-radius: 1px; background: var(--btn-dark); }
  .next-button { left: 125px; top: 422px; width: 104px; height: 44px; font-size: 16.5px; gap: 4px; }

  /* Readings screen */
  .field-label { left: 10px; font-weight: 700; font-size: 16px; letter-spacing: .2px; }
  .text-field { left: 166px; width: 175px; height: 32px; background: var(--field); border: 1px solid var(--field-line); border-radius: 2px; }
  .submit-button { left: 114px; top: 264px; width: 104px; height: 44px; font-size: 16.5px; letter-spacing: .4px; }
  .summary { left: 12px; top: 326px; width: 329px; height: 122px; background: var(--panel-grey); font-size: 14.5px; }
  .summary .row { position: absolute; left: 0; width: 100%; }
  .summary .k { position: absolute; left: 31px; }
  .summary .sep { position: absolute; left: 164px; }
  .summary .v { position: absolute; left: 186px; }
</style>
</head>
<body>

<!-- Screen: how are you feeling -->
<section class="screen screen--feeling">
  <header class="app-header">GREENLEAF CARE<br>MONITOR</header>
  <h2 class="abs feeling-title">How are you feeling?</h2>

  <svg width="0" height="0" style="position:absolute">
    <defs>
      <linearGradient id="scale-gradient" x1="0" x2="1" y1="0" y2="0">
        <stop offset="0" stop-color="#2c9e45"/>
        <stop offset=".3" stop-color="#1ba8e0"/>
        <stop offset=".55" stop-color="#f4c51a"/>
        <stop offset=".78" stop-color="#f07f1c"/>
        <stop offset="1" stop-color="#bf121b"/>
      </linearGradient>
      <g id="scale-ticks" stroke="var(--tick)" stroke-width="1">
        <line x1="7" y1="11" x2="7" y2="19"/><line x1="39" y1="11" x2="39" y2="18"/>
        <line x1="72" y1="11" x2="72" y2="18"/><line x1="104" y1="11" x2="104" y2="18"/>
        <line x1="136" y1="11" x2="136" y2="18"/><line x1="175" y1="11" x2="175" y2="18"/>
        <line x1="213" y1="11" x2="213" y2="18"/><line x1="252" y1="11" x2="252" y2="18"/>
        <line x1="291" y1="11" x2="291" y2="18"/><line x1="323" y1="11" x2="323" y2="19"/>
      </g>
    </defs>
  </svg>

  <div class="abs scale" style="top:168px">
    <svg width="330" height="22"><rect x="0" y="1" width="330" height="12" rx="6" fill="url(#scale-gradient)"/><use href="#scale-ticks"/><circle cx="72" cy="7" r="5.5" fill="none" stroke="#fff" stroke-width="1.6"/></svg>
    <span class="scale-label min">1</span><span class="scale-label name">PAIN</span><span class="scale-label max">10</span>
  </div>
  <div class="abs scale" style="top:245px">
    <svg width="330" height="22"><rect x="0" y="1" width="330" height="12" rx="6" fill="url(#scale-gradient)"/><use href="#scale-ticks"/><circle cx="50" cy="7" r="5.5" fill="none" stroke="#fff" stroke-width="1.6"/></svg>
    <span class="scale-label min">1</span><span class="scale-label name">NAUSEA</span><span class="scale-label max">10</span>
  </div>
  <div class="abs scale" style="top:322px">
    <svg width="330" height="22"><rect x="0" y="1" width="330" height="12" rx="6" fill="url(#scale-gradient)"/><use href="#scale-ticks"/><circle cx="34" cy="7" r="5.5" fill="none" stroke="#fff" stroke-width="1.6"/></svg>
    <span class="scale-label min">1</span><span class="scale-label name">SEDATION</span><span class="scale-label max">10</span>
  </div>
  <div class="abs scale" style="top:399px">
    <svg width="330" height="22"><rect x="0" y="1" width="330" height="12" rx="6" fill="url(#scale-gradient)"/><use href="#scale-ticks"/><circle cx="110" cy="7" r="5.5" fill="none" stroke="#fff" stroke-width="1.6"/></svg>
    <span class="scale-label min">1</span><span class="scale-label name">WELLBEING</span><span class="scale-label max">10</span>
  </div>

  <footer class="app-footer">Copyright © 2018 Greenleaf Care Monitor. &nbsp;All rights reserved<span class="code">M2</span></footer>
</section>

<!-- Screen: start -->
<section class="screen screen--start">
  <header class="app-header">GREENLEAF CARE<br>MONITOR</header>
  <div class="abs hero-photo" role="img" aria-label="Photo of a cannabis bud lying beside a smartphone on a wooden table"></div>
  <div class="abs pill-button start-button">
    <svg width="14" height="14" viewBox="0 0 14 14" fill="none" stroke="#fff" stroke-width="2" stroke-linecap="round"><path d="M4.2 3.4a5 5 0 1 0 5.6 0"/><line x1="7" y1="1.5" x2="7" y2="6.5"/></svg>
    START YOUR READINGS
  </div>
  <footer class="app-footer">Copyright © 2018 Greenleaf Care Monitor. &nbsp;All rights reserved<span class="code">M2</span></footer>
</section>

<!-- Screen: dose entry -->
<section class="screen screen--dose">
  <header class="app-header">GREENLEAF CARE<br>MONITOR</header>
  <h2 class="abs section-title" style="top:91px">ENTER TIME OF TAKING DRUG</h2>
  <div class="abs time-picker">
    <div class="picker-row far"><span class="c-day">Sun 28 Jan</span><span class="c-hour num">10</span><span class="c-colon">:</span><span class="c-min num">50</span></div>
    <div class="picker-row near"><span class="c-day">Mon 29 Jan</span><span class="c-hour num">11</span><span class="c-colon">:</span><span class="c-min num">55</span><span class="c-ampm">AM</span></div>
    <div class="picker-row current"><span class="c-day">Today</span><span class="divider" style="left:95px"></span><span class="c-hour num">12</span><span class="c-colon num">:</span><span class="c-min num">00</span><span class="divider" style="left:243px"></span><span class="c-ampm">PM</span></div>
    <div class="picker-row near"><span class="c-day">Wed 31 Jan</span><span class="c-hour num">1</span><span class="c-colon">:</span><span class="c-min num">05</span></div>
    <div class="picker-row far"><span class="c-day">Thu 1 Feb</span><span class="c-hour num">2</span><span class="c-colon">:</span><span class="c-min num">10</span></div>
  </div>
  <h2 class="abs section-title" style="top:291px">ENTER DOSAGE TAKEN</h2>
  <div class="abs dose-field">g</div>
  <div class="abs method" style="left:48px"><span class="box checked"></span>Tablet</div>
  <div class="abs method" style="left:149px"><span class="box"></span>Smoke</div>
  <div class="abs method" style="left:252px"><span class="box"></span>Vape</div>
  <div class="abs pill-button next-button">NEXT
    <svg width="9" height="12" viewBox="0 0 9 12" fill="none" stroke="#fff" stroke-width="2.2" stroke-linecap="round" stroke-linejoin="round"><polyline points="2,1.5 6.5,6 2,10.5"/></svg>
  </div>
  <footer class="app-footer">Copyright © 2018 Greenleaf Care Monitor. &nbsp;All rights reserved<span class="code">M2</span></footer>
</section>

<!-- Screen: readings -->
<section class="screen screen--readings">
  <header class="app-header">GREENLEAF CARE<br>MONITOR</header>
  <h2 class="abs section-title" style="top:91px">READINGS</h2>
  <div class="abs field-label" style="top:136px">PULSE</div>
  <div class="abs text-field" style="top:131px"></div>
  <div class="abs field-label" style="top:199px">BLOOD PRESSURE</div>
  <div class="abs text-field" style="top:192px"></div>
  <div class="abs pill-button submit-button">SUBMIT</div>
  <div class="abs summary">
    <div class="row" style="top:29px"><span class="k">Pulse Rate</span><span class="sep">:</span><span class="v">100 b</span></div>
    <div class="row" style="top:73px"><span class="k">Blood Pressure</span><span class="sep">:</span><span class="v">120/80</span></div>
  </div>
  <footer class="app-footer">Copyright © 2018 Greenleaf Care Monitor. &nbsp;All rights reserved<span class="code">M2</span></footer>
</section>

</body>
</html>
```